PAL-M-ERA corporate branding Powerpoint template*

We are a IT / tech company focussed on no nonsense services for our customers. Our main colors are blue and Orange as seen in the attached logo. Our catchphrase is It's palmera. We will use this template for corporate presentations at customers and potential projects.Please make sure the powerpoint does not have any art in there as the standard computers or whatsoever. We want a sleek clean design with our logo and both our colors in a main role.

Target Market(s)

Our existing customers and new customers

Industry/Entity Type

It Company

Colors

Designer to choose colors to be used in the design.

Requirements
Must have
• Different slides for different scenarios.
• Look and feel across the entire template
Nice to have
• Enough space to have our own bullet points
Should not have
• To overcrowded slides. Too loud design.

```html
<!DOCTYPE html>
<html lang="en">
<head>
<meta charset="utf-8">
<title>PAL-M-ERA Presentation Template</title>
<link href="https://fonts.googleapis.com/css2?family=Montserrat:wght@400;500;600;700;800&display=swap" rel="stylesheet">
<style>
  :root {
    --navy: #1b3f86;
    --orange: #f0711c;
    --orange-light: #f6a25a;
    --ink: #2b2b2b;
    --grey: #6a6a6a;
    --paper: #ffffff;
    --mist: #e6e6e6;
    --stage: #000000;
  }
  * { margin: 0; padding: 0; box-sizing: border-box; }
  html, body { width: 1200px; height: 696px; overflow: hidden; background: var(--stage); }
  body { position: relative; font-family: "Montserrat", Arial, sans-serif; }

  .slide {
    position: absolute; width: 586px; height: 330px; overflow: hidden;
    background: linear-gradient(100deg, #f4f4f4 0%, #ffffff 55%, #f1f1f1 100%);
  }
  .slide--a { left: 10px; top: 14px; }
  .slide--b { left: 605px; top: 14px; }
  .slide--c { left: 10px; top: 352px; background: var(--paper); }
  .slide--d { left: 605px; top: 352px; }

  .slide__backdrop { position: absolute; inset: 0; }
  .slide__panel { position: absolute; inset: 0; width: 586px; height: 330px; }
  .slide__band { position: absolute; left: 0; right: 0; bottom: 0; height: 10px; background: var(--navy); }

  .cover-title {
    position: absolute; right: 14px; top: 154px; text-align: right;
    font-weight: 800; font-size: 31px; line-height: 35px; letter-spacing: 0.5px;
  }
  .cover-title__first { color: var(--navy); display: block; }
  .cover-title__second { color: var(--ink); display: block; }
  .cover-rule { position: absolute; right: 14px; top: 234px; width: 184px; height: 2px; background: var(--orange); }
  .brand { position: absolute; right: 14px; top: 246px; text-align: right; }
  .brand__name { font-weight: 800; font-size: 36px; line-height: 40px; color: var(--navy); letter-spacing: 0.5px; }
  .brand__tag { font-weight: 400; font-size: 12px; letter-spacing: 7.4px; color: var(--ink); text-transform: uppercase; margin-right: -7px; }

  .mini-brand { position: absolute; right: 10px; top: 9px; text-align: right; }
  .mini-brand__name { font-weight: 800; font-size: 14px; line-height: 16px; color: var(--navy); }
  .mini-brand__tag { font-size: 5px; letter-spacing: 2.4px; color: var(--grey); text-transform: uppercase; margin-right: -2px; }

  .content { position: absolute; left: 320px; top: 72px; width: 250px; }
  .content__heading { font-weight: 800; font-size: 17px; color: var(--orange); line-height: 20px; }
  .content__intro { font-size: 8.5px; line-height: 13px; color: var(--grey); margin-top: 5px; }
  .point { position: relative; padding-left: 20px; margin-top: 14px; }
  .point:first-of-type { margin-top: 14px; }
  .point__marker { position: absolute; left: 2px; top: 3px; width: 8px; height: 8px; background: var(--orange); }
  .point__title { font-weight: 700; font-size: 11.5px; color: var(--navy); line-height: 14px; }
  .point__text { font-size: 7px; line-height: 10.5px; color: var(--grey); margin-top: 4px; }

  .footer { position: absolute; left: 0; right: 0; bottom: 0; height: 16px; }
  .footer__copy { position: absolute; left: 6px; bottom: 3px; font-size: 7.5px; color: #fff; }
  .footer__page { position: absolute; right: 14px; bottom: 3px; font-size: 7.5px; color: #fff; }
</style>
</head>
<body>

  <!-- Cover, warm gradient variant -->
  <section class="slide slide--a">
    <svg class="slide__panel" viewBox="0 0 586 330" role="img" aria-label="Photo of network cables plugged into a server switch, warm orange tint">
      <defs>
        <linearGradient id="warmPhoto" x1="0" y1="0" x2="1" y2="1">
          <stop offset="0" stop-color="#ea8a3c"/>
          <stop offset="0.6" stop-color="#e79a44"/>
          <stop offset="1" stop-color="#c98a52"/>
        </linearGradient>
      </defs>
      <polygon points="0,0 336,0 194,320 0,320" fill="url(#warmPhoto)"/>
    </svg>
    <h1 class="cover-title"><span class="cover-title__first">PRESENTATION</span><span class="cover-title__second">TITLE HERE</span></h1>
    <div class="cover-rule"></div>
    <div class="brand"><div class="brand__name">PAL-M-ERA</div><div class="brand__tag">It's palmera</div></div>
    <div class="slide__band"></div>
  </section>

  <!-- Cover, duotone variant -->
  <section class="slide slide--b">
    <svg class="slide__panel" viewBox="0 0 586 330" role="img" aria-label="Photo of network cables in a server switch, brown duotone with orange accent">
      <defs>
        <linearGradient id="duoPhoto" x1="0" y1="0" x2="1" y2="1">
          <stop offset="0" stop-color="#8e6a55"/>
          <stop offset="0.5" stop-color="#a9684a"/>
          <stop offset="1" stop-color="#e0601f"/>
        </linearGradient>
      </defs>
      <polygon points="0,0 356,0 206,320 0,320" fill="url(#duoPhoto)"/>
    </svg>
    <h1 class="cover-title"><span class="cover-title__first">PRESENTATION</span><span class="cover-title__second">TITLE HERE</span></h1>
    <div class="cover-rule"></div>
    <div class="brand"><div class="brand__name">PAL-M-ERA</div><div class="brand__tag">It's palmera</div></div>
    <div class="slide__band"></div>
  </section>

  <!-- Content slide with bullet points -->
  <section class="slide slide--c">
    <svg class="slide__panel" viewBox="0 0 586 330">
      <defs>
        <linearGradient id="deskPhoto" x1="0" y1="0" x2="1" y2="1">
          <stop offset="0" stop-color="#2c3540"/>
          <stop offset="0.6" stop-color="#3d4b58"/>
          <stop offset="1" stop-color="#6f7780"/>
        </linearGradient>
      </defs>
      <polygon points="0,0 326,0 232,314 0,314" fill="url(#deskPhoto)" role="img" aria-label="Photo of a laptop screen showing code"/>
      <polygon points="290,134 297,137 232,314 222,314" fill="var(--orange)"/>
      <polygon points="0,314 506,314 512,330 0,330" fill="var(--navy)"/>
      <polygon points="512,314 586,314 586,330 518,330" fill="var(--orange)"/>
      <rect x="582" y="0" width="4" height="34" fill="var(--navy)"/>
    </svg>
    <div class="mini-brand"><div class="mini-brand__name">PAL-M-ERA</div><div class="mini-brand__tag">It's palmera</div></div>
    <div class="content">
      <h2 class="content__heading">BULLET POINTS TEXT HERE</h2>
      <p class="content__intro">Lorem ipsum dolor sit amet, consectetur adipi scing elit, sed do eiusmod tempor incididunt ut labore</p>
      <div class="point"><span class="point__marker"></span><h3 class="point__title">BULLET POINT TITLE HERE</h3><p class="point__text">Lorem ipsum dolor sit amet, consectetur adipisicing elit, sed do eiusmod tempor incididunt ut labor aliqua. Lorem ipsum dolor sit amet, consectetur adipisicing elit.</p></div>
      <div class="point"><span class="point__marker"></span><h3 class="point__title">BULLET POINT TITLE HERE</h3><p class="point__text">Lorem ipsum dolor sit amet, consectetur adipisicing elit, sed do eiusmod tempor incididunt ut labor aliqua. Lorem ipsum dolor sit amet, consectetur adipisicing elit.</p></div>
      <div class="point"><span class="point__marker"></span><h3 class="point__title">BULLET POINT TITLE HERE</h3><p class="point__text">Lorem ipsum dolor sit amet, consectetur adipisicing elit, sed do eiusmod tempor incididunt ut labor aliqua. Lorem ipsum dolor sit amet, consectetur adipisicing elit.</p></div>
    </div>
    <div class="footer"><span class="footer__copy">Copyright text here</span><span class="footer__page">Page : 01</span></div>
  </section>

  <!-- Cover, light variant -->
  <section class="slide slide--d">
    <div class="slide__backdrop" role="img" aria-label="Faded grey photo of network cables" style="background: linear-gradient(110deg, #d9d9d9 0%, #e8e8e8 45%, #f2f2f2 100%);"></div>
    <h1 class="cover-title"><span class="cover-title__first">PRESENTATION</span><span class="cover-title__second">TITLE HERE</span></h1>
    <div class="cover-rule"></div>
    <div class="brand"><div class="brand__name">PAL-M-ERA</div><div class="brand__tag">It's palmera</div></div>
    <div class="slide__band"></div>
  </section>

</body>
</html>
```